Business Card Design Project

Looking to have a new business card created.

The card needs to be sort of two cards attached in the centre creating a flip card so we can write in the centre.

First side with my information at the director / licensee and then the back side with my assistant's details.

Inside with minimal information, facebook link/sign and then lines to write on.

www.kestrelhomeservices.com.au is my website to show colours and designs that I like.
Updates

Target Market(s)

Property Owners, Property Investors, Tenants, rental clients, Tradesman.

Industry/Entity Type

Business

Requirements
Must have
• Professional & symmetrical.

Am getting pro photos for myself & assistance, so a space for these once received.

```html
<!DOCTYPE html>
<html lang="en">
<head>
<meta charset="utf-8">
<title>Business Card Design</title>
<link rel="stylesheet" href="https://fonts.googleapis.com/css2?family=Caladea&family=Questrial&display=swap">
<style>
  :root {
    --page: #ffffff;
    --ink: #111111;
    --band-dark: #0e1719;
    --band-glow: #1f4751;
    --card-text: #e8eef0;
    --card-muted: #c9d3d6;
    --brand: #a9bcc2;
    --brand-faint: #e6e9ea;
    --rule: #e2e4e5;
    --strip: #14211f;
  }
  * { margin: 0; padding: 0; box-sizing: border-box; }
  html, body { width: 1200px; height: 900px; overflow: hidden; background: var(--page); }
  .sheet { position: relative; width: 1200px; height: 900px; font-family: "Caladea", Georgia, serif; color: var(--ink); }
  .sheet-title { position: absolute; top: 93px; left: 0; width: 1200px; text-align: center; font-size: 18px; }
  .view-label { position: absolute; font-size: 14px; text-align: center; width: 200px; }

  .card { position: absolute; top: 153px; width: 425px; height: 240px; overflow: hidden; font-family: "Questrial", Arial, sans-serif; }
  .card--back { left: 175px; }
  .card--front { left: 600px; }
  .portrait { position: absolute; top: 0; left: 0; width: 425px; height: 142px;
    background: linear-gradient(90deg, #f1f3f4 0%, #dfe4e6 20%, #eef0f0 40%, #caa58f 62%, #8a5a3e 78%, #e8eaeb 100%); }
  .info-band { position: absolute; top: 142px; left: 0; width: 425px; height: 98px;
    background: radial-gradient(ellipse 260px 90px at 120px 45px, var(--band-glow) 0%, var(--band-dark) 80%); }
  .brand-name { position: absolute; color: var(--brand); font-family: "Questrial", Arial, sans-serif; white-space: nowrap; }
  .info-band .brand-name { left: 40px; top: 33px; font-size: 24px; letter-spacing: 0.5px; }
  .brand-mark { display: inline-block; width: 10px; height: 10px; background: var(--brand); margin-left: 6px; vertical-align: 4px; }
  .contact { position: absolute; left: 195px; top: 12px; color: var(--card-text); font-size: 9px; line-height: 10.5px; }
  .contact-name { font-size: 13px; line-height: 16px; }
  .contact-role { color: var(--card-muted); margin-bottom: 9px; }
  .contact-row span { display: inline-block; width: 52px; }

  .score-note { position: absolute; left: 500px; top: 434px; width: 200px; text-align: center; font-size: 14px; line-height: 17px; }
  .score-arrows { position: absolute; left: 590px; top: 395px; }

  .inside { position: absolute; top: 507px; left: 175px; width: 850px; height: 239px; font-family: "Questrial", Arial, sans-serif; }
  .notes-strip { position: absolute; left: 0; top: 0; width: 24px; height: 239px;
    background: linear-gradient(180deg, #0c1413, #1d302d 50%, #0c1413); }
  .notes-lines { position: absolute; left: 49px; top: 0; }
  .inside .brand-name--faint { left: 128px; top: 98px; font-size: 42px; color: var(--brand-faint); }
  .brand-name--faint .brand-mark { background: var(--brand-faint); width: 16px; height: 16px; vertical-align: 8px; }
  .room-photo { position: absolute; left: 376px; width: 171px; }
  .room-photo--kitchen { top: 0; height: 72px; background: linear-gradient(135deg, #cfd2d1, #f3f3f1 45%, #3b3431 80%, #6a625c); }
  .room-photo--bedroom { top: 74px; height: 91px; background: linear-gradient(180deg, #dfe2e4, #f4f4f3 50%, #6d4e3c 75%, #e9e7e4); }
  .room-photo--living { top: 167px; height: 72px; background: linear-gradient(135deg, #e9ebe8, #9fae8d 50%, #f1f0ec 70%, #4b3f36); }
  .company-panel { position: absolute; left: 547px; top: 0; width: 303px; height: 239px;
    background: radial-gradient(ellipse 200px 120px at 150px 80px, var(--band-glow) 0%, var(--band-dark) 85%);
    color: var(--card-text); text-align: center; font-size: 9px; }
  .company-panel .brand-name { left: 0; width: 303px; text-align: center; top: 45px; font-size: 34px; }
  .company-panel .brand-name .brand-mark { width: 13px; height: 13px; vertical-align: 6px; }
  .company-details { position: absolute; top: 119px; left: 0; width: 303px; line-height: 12px; }
  .company-details p { margin: 0; }
  .company-details .gap { margin-top: 5px; }
  .company-details strong { font-weight: 400; color: #ffffff; }
</style>
</head>
<body>
<main class="sheet">
  <h1 class="sheet-title" style="font-weight:400">Business Card Design</h1>

  <section class="card card--back">
    <div class="portrait" role="img" aria-label="Portrait photo of the rental manager"></div>
    <div class="info-band">
      <div class="brand-name">kestrel<span class="brand-mark"></span></div>
      <div class="contact">
        <div class="contact-name">Clara Whitmore</div>
        <div class="contact-role">Rental Manager</div>
        <div class="contact-row"><span>Telephone</span>1300 555 210</div>
        <div class="contact-row"><span>Mobile</span>0400 555 318</div>
        <div class="contact-row">clara@kestrelhomeservices.com.au</div>
      </div>
    </div>
  </section>

  <section class="card card--front">
    <div class="portrait" role="img" aria-label="Portrait photo of the managing director"></div>
    <div class="info-band">
      <div class="brand-name">kestrel<span class="brand-mark"></span></div>
      <div class="contact">
        <div class="contact-name">Nora Bellamy</div>
        <div class="contact-role">Managing Director, Principal REA</div>
        <div class="contact-row"><span>Telephone</span>1300 555 210</div>
        <div class="contact-row"><span>Mobile</span>0400 555 642</div>
        <div class="contact-row">nora@kestrelhomeservices.com.au</div>
      </div>
    </div>
  </section>

  <div class="view-label" style="left:288px;top:405px">Back Side View</div>
  <div class="view-label" style="left:713px;top:405px">Front Side View</div>

  <svg class="score-arrows" width="20" height="112" viewBox="0 0 20 112" aria-hidden="true">
    <line x1="10" y1="4" x2="10" y2="34" stroke="#111" stroke-width="1"/>
    <path d="M6 9 L10 2 L14 9 Z" fill="#111"/>
    <line x1="10" y1="76" x2="10" y2="106" stroke="#111" stroke-width="1"/>
    <path d="M6 101 L10 108 L14 101 Z" fill="#111"/>
  </svg>
  <div class="score-note">Scoring<br>Here</div>

  <section class="inside">
    <div class="notes-strip"></div>
    <svg class="notes-lines" width="304" height="239" viewBox="0 0 304 239" aria-hidden="true">
      <g stroke="#e2e4e5" stroke-width="1">
        <line x1="0" y1="34" x2="304" y2="34"/>
        <line x1="0" y1="58" x2="304" y2="58"/>
        <line x1="0" y1="82" x2="304" y2="82"/>
        <line x1="0" y1="107" x2="304" y2="107"/>
        <line x1="0" y1="131" x2="304" y2="131"/>
        <line x1="0" y1="156" x2="304" y2="156"/>
        <line x1="0" y1="180" x2="304" y2="180"/>
        <line x1="0" y1="205" x2="304" y2="205"/>
      </g>
    </svg>
    <div class="brand-name brand-name--faint">kestrel<span class="brand-mark"></span></div>

    <div class="room-photo room-photo--kitchen" role="img" aria-label="Photo of a modern white kitchen"></div>
    <div class="room-photo room-photo--bedroom" role="img" aria-label="Photo of a furnished bedroom"></div>
    <div class="room-photo room-photo--living" role="img" aria-label="Photo of a bright living room"></div>

    <div class="company-panel">
      <div class="brand-name">kestrel<span class="brand-mark"></span></div>
      <div class="company-details">
        <p><strong>Apply online:</strong> http://bit.ly/kesths</p>
        <p>1300 KESTREL</p>
        <p><strong>ACN:</strong> 482 615 903</p>
        <p class="gap"><strong>Postal Address:</strong> PO Box 418, Brookvale Q 4510</p>
        <p class="gap"><strong>Office Location:</strong> Level 2/8 Harbour Lane, Brookvale Q 4510</p>
        <p class="gap">www.kestrelhomeservices.com.au</p>
      </div>
    </div>
  </section>

  <div class="view-label" style="left:500px;top:759px">Inside View</div>
</main>
</body>
</html>
```